Display Layouts per segment use-cases

21.5in portrait (9:16) x 2
Office towers
Hotels
Shopping Malls

Target Market(s)

Office towers / Hotels / Shopping Malls

```html
<!DOCTYPE html>
<html lang="en">
<head>
<meta charset="utf-8">
<title>Lobby Display – Hotel Corridor</title>
<link href="https://fonts.googleapis.com/css2?family=Quicksand:wght@400;500;600;700&display=swap" rel="stylesheet">
<style>
  :root {
    --white: #ffffff;
    --orange: #d95f0e;
    --orange-dark: #b8541a;
    --wood-dark: #6e2a0e;
    --wood: #a84a16;
    --wall-gold: #b88a2a;
    --ceiling: #5a2e18;
    --light-warm: #f0c89a;
    --floor: #d9ad84;
    --floor-light: #e6c3a0;
    --panel-top: rgba(104, 72, 56, 0.9);
    --panel-mid: rgba(118, 86, 68, 0.82);
    --panel-bottom: rgba(172, 142, 116, 0.78);
    --rule: rgba(255, 255, 255, 0.45);
  }
  * { margin: 0; padding: 0; box-sizing: border-box; }
  html, body { width: 675px; height: 1200px; overflow: hidden; background: #3a2418; }
  .display {
    position: relative;
    width: 675px;
    height: 1200px;
    overflow: hidden;
    font-family: "Quicksand", sans-serif;
    color: var(--white);
  }
  .corridor-photo {
    position: absolute;
    inset: 0;
    background:
      radial-gradient(ellipse 14% 10% at 48% 34%, rgba(255,226,180,0.85) 0%, rgba(255,226,180,0) 100%),
      linear-gradient(180deg, var(--ceiling) 0%, rgba(90,46,24,0.75) 14%, rgba(90,46,24,0) 30%),
      linear-gradient(180deg, rgba(217,173,132,0) 45%, rgba(217,173,132,0.7) 70%, var(--floor-light) 100%),
      linear-gradient(90deg, var(--wood-dark) 0%, var(--wood) 8%, var(--wall-gold) 16%, #a0521e 28%, #c98a55 40%, var(--floor) 55%, #c9945e 64%, var(--light-warm) 100%);
  }
  .info-panel {
    position: absolute;
    left: 417px;
    top: 0;
    width: 258px;
    height: 1200px;
    background: linear-gradient(180deg, var(--panel-top) 0%, var(--panel-mid) 55%, var(--panel-bottom) 100%);
  }
  .brand-name {
    position: absolute;
    right: 30px;
    top: 64px;
    font-size: 56px;
    font-weight: 700;
    letter-spacing: -2px;
    line-height: 1;
  }
  .weather-icon {
    position: absolute;
    left: 456px;
    top: 322px;
    width: 164px;
    height: 126px;
  }
  .temperature {
    position: absolute;
    left: 458px;
    top: 452px;
    font-size: 90px;
    font-weight: 500;
    line-height: 1;
    letter-spacing: -3px;
  }
  .temperature .unit {
    font-size: 62px;
    font-weight: 400;
    letter-spacing: 0;
    margin-left: 4px;
  }
  .clock {
    position: absolute;
    left: 456px;
    top: 632px;
    font-size: 57px;
    font-weight: 600;
    line-height: 1;
    letter-spacing: -2px;
  }
  .clock .meridiem {
    font-size: 25px;
    font-weight: 400;
    letter-spacing: 0;
    vertical-align: top;
    position: relative;
    top: 1px;
  }
  .date-rule {
    position: absolute;
    left: 460px;
    top: 697px;
    width: 173px;
    height: 1px;
    background: var(--rule);
  }
  .weekday {
    position: absolute;
    left: 459px;
    top: 704px;
    font-size: 23px;
    font-weight: 400;
    letter-spacing: -0.5px;
  }
  .date {
    position: absolute;
    left: 458px;
    top: 729px;
    font-size: 35px;
    font-weight: 700;
    letter-spacing: -1.2px;
  }
  .floor-badge {
    position: absolute;
    left: 30px;
    top: 866px;
    width: 320px;
    height: 320px;
  }
</style>
</head>
<body>
<main class="display">
  <div class="corridor-photo" role="img" aria-label="Photo: long, warmly lit hotel corridor with wooden doors, golden walls, ceiling spotlights and a tiled floor"></div>

  <aside class="info-panel"></aside>

  <h1 class="brand-name">LIFTORA</h1>

  <svg class="weather-icon" viewBox="0 0 164 126" aria-label="Partly cloudy">
    <g stroke="var(--white)" stroke-width="3.5" stroke-linecap="round" fill="none">
      <line x1="46" y1="2" x2="46" y2="14"/>
      <line x1="14" y1="14" x2="23" y2="24"/>
      <line x1="78" y1="14" x2="69" y2="24"/>
      <line x1="2" y1="44" x2="15" y2="44"/>
      <line x1="14" y1="76" x2="22" y2="68"/>
    </g>
    <circle cx="47" cy="45" r="23" fill="var(--white)"/>
    <path d="M22 122 C4 122 4 92 26 90 C28 74 46 66 60 74 C68 50 104 46 116 70 C134 68 150 82 148 98 C164 104 160 122 144 122 Z"
          fill="var(--white)" stroke="#8a5a3e" stroke-width="3"/>
  </svg>

  <div class="temperature">18°<span class="unit">C</span></div>

  <div class="clock">14:44<span class="meridiem">PM</span></div>
  <div class="date-rule"></div>
  <div class="weekday">SUNDAY</div>
  <div class="date">25 AUGUST</div>

  <svg class="floor-badge" viewBox="0 0 320 320" aria-label="Floor 12, going up">
    <circle cx="155" cy="155" r="146" fill="var(--orange)"/>
    <circle cx="163" cy="166" r="145" fill="var(--white)" stroke="#b8541a" stroke-width="1.5"/>
    <polygon points="156,32 79,190 156,150" fill="var(--orange)"/>
    <polygon points="156,32 231,190 156,150" fill="var(--orange-dark)"/>
    <text x="156" y="272" text-anchor="middle" font-family="Quicksand, sans-serif" font-weight="700" font-size="112" fill="var(--orange)" letter-spacing="-4">12</text>
  </svg>
</main>
</body>
</html>
```